Fallow Crest Bourbon Barrel Aged Wine

We are taking a sweet red wine and barrel aging it in previously used bourbon barrels. The abv is 16%. Kentucky based. I have attached our Brand logo for reference. Use colors that evoke warmth, richness, and sophistication. We would like to consider a raised or textured label.

Target Market(s)

bourbon and wine drinkers

```html
<!DOCTYPE html>
<html lang="en">
<head>
<meta charset="utf-8">
<title>Fallow Crest Red Wine Blend Label</title>
<link rel="stylesheet" href="https://fonts.googleapis.com/css2?family=Cinzel:wght@500;600&family=EB+Garamond:wght@500&display=swap">
<style>
  :root {
    --backdrop: #121410;
    --label-green: #5f7452;
    --label-green-deep: #4f6444;
    --foil-gold: #cfac55;
    --foil-gold-light: #ecd58f;
    --foil-gold-dark: #9b7a2e;
    --wine-red: #b6323b;
    --ink-dark: #26271f;
  }
  html, body {
    margin: 0;
    width: 1200px;
    height: 1200px;
    overflow: hidden;
    background: var(--backdrop);
  }
  .canvas {
    position: relative;
    width: 1200px;
    height: 1200px;
  }
  .label-shape {
    position: absolute;
    inset: 0;
  }
  .label-text {
    position: absolute;
    left: 0;
    width: 1200px;
    text-align: center;
    margin: 0;
  }
  .brand-mark {
    top: 292px;
    font-family: "Cinzel", serif;
    font-weight: 600;
    font-size: 28px;
    letter-spacing: 5px;
    color: var(--foil-gold);
  }
  .product-name {
    top: 398px;
    font-family: "Cinzel", serif;
    font-weight: 600;
    font-size: 64px;
    letter-spacing: 3px;
    color: var(--foil-gold);
  }
  .wine-style {
    top: 490px;
    font-family: "Cinzel", serif;
    font-weight: 500;
    font-size: 46px;
    letter-spacing: 3px;
    color: var(--wine-red);
  }
  .aging-note {
    top: 568px;
    font-family: "EB Garamond", serif;
    font-weight: 500;
    font-size: 32px;
    line-height: 1.15;
    letter-spacing: 3px;
    text-transform: uppercase;
    color: var(--ink-dark);
  }
  .bottle-facts {
    position: absolute;
    top: 680px;
    left: 304px;
    margin: 0;
    font-family: "EB Garamond", serif;
    font-weight: 500;
    font-size: 19px;
    line-height: 1.35;
    letter-spacing: 1px;
    color: var(--ink-dark);
  }
</style>
</head>
<body>
<main class="canvas">
  <svg class="label-shape" width="1200" height="1200" viewBox="0 0 1200 1200">
    <defs>
      <linearGradient id="foil" x1="0" y1="0" x2="1" y2="1">
        <stop offset="0" stop-color="var(--foil-gold-light)"/>
        <stop offset="0.5" stop-color="var(--foil-gold)"/>
        <stop offset="1" stop-color="var(--foil-gold-dark)"/>
      </linearGradient>
      <linearGradient id="landscape-tone" x1="0" y1="0" x2="0" y2="1">
        <stop offset="0" stop-color="var(--label-green)"/>
        <stop offset="1" stop-color="#9a8649"/>
      </linearGradient>
      <clipPath id="label-inner">
        <path d="M282 390 C282 205 440 132 600 132 C760 132 918 205 918 390 L918 700 C918 885 770 1010 600 1066 C430 1010 282 885 282 700 Z"/>
      </clipPath>
    </defs>

    <path class="label-border" fill="url(#foil)"
      d="M250 380 C250 180 420 100 600 100 C780 100 950 180 950 380 L950 700 C950 905 790 1040 600 1100 C410 1040 250 905 250 700 Z"/>
    <path class="label-field" fill="var(--label-green)"
      d="M264 384 C264 192 428 114 600 114 C772 114 936 192 936 384 L936 700 C936 895 782 1026 600 1085 C418 1026 264 895 264 700 Z"/>

    <g clip-path="url(#label-inner)">
      <rect class="landscape-area" role="img" aria-label="Gold foil line illustration of rolling Kentucky hills"
        x="260" y="760" width="680" height="340" fill="url(#landscape-tone)"/>
    </g>

    <path class="label-inner-rule" fill="none" stroke="var(--foil-gold)" stroke-width="2"
      d="M282 390 C282 205 440 132 600 132 C760 132 918 205 918 390 L918 700 C918 885 770 1010 600 1066 C430 1010 282 885 282 700 Z"/>

    <circle class="brand-ring" cx="600" cy="215" r="52" fill="none" stroke="var(--foil-gold)" stroke-width="4"/>
  </svg>

  <p class="label-text brand-mark">Fallow Crest</p>
  <h1 class="label-text product-name">FALLOW CREST</h1>
  <h2 class="label-text wine-style">RED WINE BLEND</h2>
  <p class="label-text aging-note">Aged in Kentucky<br>Bourbon Barrels</p>
  <p class="bottle-facts">16% ABV<br>750 ML</p>
</main>
</body>
</html>
```